Engineering Consultant Business Card

I'm starting a new business as a high-end engineering consultant in a niche field. I've attached the jpg for my logo plus the branding guideline document that I've been following. You can see my business website here: www.orvalink.com
I'd like a business card that has the logo on one side, then the other side has (in any order): Tessmor Pact, Inc.
Delia Whitcombe
President and Chief EMC Engineer
www.orvalink.com
delia@orvalink.com
Optional: motto "We will solve your EMC problems as early as possible—ideally before they even start."
I'm not planning on including a phone number
Target Market(s)
Businesses, especially makers of electronics hardware
Industry/Entity Type
Electrical engineering
Contact Information for Business Card
Company name, my name, website, email
Look and feel
Each slider illustrates characteristics of the customer's brand and the style your logo design should communicate.

```html
<!DOCTYPE html>
<html lang="en">
<head>
<meta charset="utf-8">
<title>Tessmor Pact, Inc. — Business Card</title>
<link rel="stylesheet" href="https://fonts.googleapis.com/css2?family=Inter:wght@500;700&family=Tinos&display=swap">
<style>
  :root {
    --navy: #2e4495;
    --cyan: #4aa9cf;
    --cyan-light: #7ac4d6;
    --paper: #e9f3f5;
    --ink: #0b0b0f;
    --white: #ffffff;
    --page: #ffffff;
  }
  * { margin: 0; padding: 0; box-sizing: border-box; }
  html, body { width: 1153px; height: 1200px; overflow: hidden; background: var(--page); }
  body { position: relative; font-family: "Inter", Arial, sans-serif; }

  .card {
    position: absolute;
    left: 325px;
    width: 556px;
    height: 334px;
    overflow: hidden;
  }
  .card--front { top: 214px; background: var(--navy); }
  .card--back { top: 639px; background: var(--paper); }

  /* Front */
  .circuit-band {
    position: absolute;
    left: 0;
    width: 100%;
  }
  .circuit-band--top {
    top: 0; height: 112px;
    background: linear-gradient(180deg, rgba(74,169,207,0.32) 0%, rgba(74,169,207,0.12) 60%, rgba(74,169,207,0) 100%);
  }
  .circuit-band--bottom {
    bottom: 0; height: 130px;
    background: linear-gradient(0deg, rgba(74,169,207,0.32) 0%, rgba(74,169,207,0.12) 60%, rgba(74,169,207,0) 100%);
  }
  .brand-name {
    position: absolute;
    left: 0; right: 0;
    top: 143px;
    text-align: center;
    color: var(--white);
    font-weight: 700;
    font-size: 40px;
    line-height: 48px;
    letter-spacing: -0.5px;
  }

  /* Back */
  .back-shapes { position: absolute; inset: 0; width: 100%; height: 100%; }
  .circuit-panel {
    position: absolute;
    inset: 0;
    clip-path: polygon(0 0, 223px 0, 143px 100%, 0 100%);
    background:
      linear-gradient(180deg, rgba(74,169,207,0.28) 0%, rgba(74,169,207,0.08) 32%, rgba(74,169,207,0) 45%, rgba(74,169,207,0) 62%, rgba(74,169,207,0.1) 75%, rgba(74,169,207,0.28) 100%);
  }
  .company {
    position: absolute;
    left: 16px; top: 129px;
    color: var(--white);
    font-weight: 700;
    font-size: 18px;
    line-height: 24px;
    letter-spacing: -0.3px;
    white-space: nowrap;
  }
  .motto {
    position: absolute;
    left: 16px; top: 158px;
    width: 156px;
    color: var(--white);
    font-family: "Tinos", "Times New Roman", serif;
    font-size: 12.5px;
    line-height: 11px;
    text-align: justify;
  }
  .person-name {
    position: absolute;
    left: 248px; top: 82px;
    color: var(--ink);
    font-weight: 700;
    font-size: 32px;
    line-height: 40px;
    letter-spacing: -0.6px;
    white-space: nowrap;
  }
  .person-title {
    position: absolute;
    left: 249px; top: 118px;
    color: var(--ink);
    font-weight: 500;
    font-size: 17px;
    line-height: 22px;
    white-space: nowrap;
  }
  .title-rule {
    position: absolute;
    left: 248px; top: 145px;
    width: 223px; height: 7px;
    background: linear-gradient(90deg, var(--navy), var(--cyan));
  }
  .contacts {
    position: absolute;
    left: 248px; top: 218px;
    list-style: none;
  }
  .contact {
    display: flex;
    align-items: center;
    height: 21px;
    font-family: "Tinos", "Times New Roman", serif;
    font-size: 17px;
    color: var(--ink);
  }
  .contact-icon { width: 17px; height: 17px; margin-right: 15px; flex: none; }
</style>
</head>
<body>

  <section class="card card--front" aria-label="Card front">
    <div class="circuit-band circuit-band--top" role="img" aria-label="Circuit trace line pattern"></div>
    <div class="circuit-band circuit-band--bottom" role="img" aria-label="Circuit trace line pattern"></div>
    <p class="brand-name">Tessmor Pact</p>
  </section>

  <section class="card card--back" aria-label="Card back">
    <svg class="back-shapes" viewBox="0 0 919 552" preserveAspectRatio="none" aria-hidden="true">
      <polygon points="0,0 404,0 272,552 0,552" fill="var(--navy)"/>
      <polygon points="369,0 388,0 254,552 237,552" fill="var(--cyan-light)"/>
      <polygon points="388,0 396,0 262,552 254,552" fill="var(--cyan)"/>
    </svg>
    <div class="circuit-panel" role="img" aria-label="Diagonal circuit trace line pattern"></div>

    <h2 class="company">Tessmor Pact, Inc.</h2>
    <p class="motto">We will solve your EMC problems as early as possible—ideally before they even start.</p>

    <h1 class="person-name">Delia Whitcombe</h1>
    <p class="person-title">President and Chief EMC Engineer</p>
    <div class="title-rule"></div>

    <ul class="contacts">
      <li class="contact">
        <svg class="contact-icon" viewBox="0 0 20 20" aria-hidden="true">
          <circle cx="10" cy="10" r="9" fill="var(--navy)"/>
          <circle cx="10" cy="10" r="6.5" fill="none" stroke="var(--white)" stroke-width="1.2"/>
          <path d="M5 8 Q8 6 9 9 Q8 12 11 12 L12 15 M11 5 Q14 7 15 10" fill="none" stroke="var(--white)" stroke-width="1.4"/>
        </svg>
        <span>www.orvalink.com</span>
      </li>
      <li class="contact">
        <svg class="contact-icon" viewBox="0 0 20 20" aria-hidden="true">
          <rect x="1" y="4" width="18" height="12" fill="var(--navy)"/>
          <path d="M1 4 L10 11 L19 4 M1 16 L8 9.5 M19 16 L12 9.5" fill="none" stroke="var(--white)" stroke-width="1"/>
        </svg>
        <span>delia@orvalink.com</span>
      </li>
    </ul>
  </section>

</body>
</html>
```